Generator Control - Superyacht Power Management System

We need a graphic design for a Touch Screen interface to control generators on Superyachts. We have a layout of the control system worked out, but need nice graphics to go with it.
The graphics comes down to a 300x460px App that i replicate several times on my 15" touchscreen as required.
See attached images.
The interface is divided up into 4 sections:
• Section#1 - 4 rectangles for the control
• Section#2 - a vertical bar graph,
• Section#3 - a section to display custom information
• Section#4 - a circuit breaker symbol.
The dimensions in pixels must be as per the attached image.
SECTION#1:
The 4 control rectangles correspond to 4 control modes:
• STOP – colours based on RED
• RUN – colours based on ORANGE
• RUN ONLINE – colours based on GREEN
• AUTO – colours based on BLUE
• THE TEXT DOESN’T HAVE TO BE ON THE GRAPHICS, WE JUST NEED THE BACKGROUND FOR THE TEXT, I ADD THE TEXT LATER USING SOFTWARE.
Each control rectangle needs to have 3 clearly identifiable states:
• Active/Selected (this is the currently active mode)
• Not Active/Not Selected (this mode is available but not currently active)
• Unavailable (this mode is not available)
SECTION#2:
The vertical bar graph design only needs the outline/frame of the bar graph. The actual moving part can be left blank; I will add that in later using an animation.
SECTION#3:
Free to look good as you want. See attached image for reference.
Within section#3 (at the top) is a 40x240px subsection, and should simply by 2 states, green or 'background colour of section#3 '. (green for when the generator is running, blend with the rest of section#3 when it is not). There are about 10 different texts I add on top of that square using software, corresponding to the status of the generator (starting, deloading, synchronizing, etc.)
SECTION#4:
Graphical representation of an electrical switch. Can be in two positions: opened or closed. See attached image as reference.

Target Market(s)

Cheif Engineers /Captains on Superyachts

Industry/Entity Type

Graphic Design

Requirements
Must have
• Must have the same graphics style as the uploaded file#2

```html
<!DOCTYPE html>
<html lang="en">
<head>
<meta charset="utf-8">
<title>Generator Control Panels</title>
<link rel="stylesheet" href="https://fonts.googleapis.com/css2?family=Open+Sans:wght@400;600;700&display=swap">
<style>
:root{
  --bg:#262626;
  --bg-line:#2c2c2c;
  --panel-white:#ffffff;
  --btn-top:#ffffff;
  --btn-bottom:#e6e6e6;
  --btn-border:#c9c9c9;
  --off-top:#cfcfcf;
  --off-bottom:#a8a8a8;
  --off-border:#f2f2f2;
  --off-text:#7d7d7d;
  --header-top:#3e4c5c;
  --header-bottom:#2b3744;
  --text-dark:#3a3a3a;
  --text-mid:#777777;
  --rule:#d4d4d4;
  --scale-bg:#f4f4f4;
  --green:#7ac231;
  --green-dark:#5ea21c;
  --green-light:#95d64d;
  --red:#d8231c;
  --orange:#f0a20c;
  --blue:#2f7fd0;
  --navy:#0f3a7a;
}
*{box-sizing:border-box;margin:0;padding:0}
html,body{width:1200px;height:733px;overflow:hidden}
body{
  font-family:"Open Sans",Arial,sans-serif;
  background:var(--bg);
  background-image:repeating-linear-gradient(45deg,var(--bg-line) 0 1px,transparent 1px 4px),
                   repeating-linear-gradient(-45deg,var(--bg-line) 0 1px,transparent 1px 4px);
  position:relative;
}
.panel{position:absolute;top:0;width:400px;height:733px}
.panel--offline{left:148px}
.panel--online{left:659px}

.breaker{
  position:absolute;left:155px;top:60px;width:80px;height:132px;
  background:linear-gradient(#fbfbfb,#ececec);
  border:1px solid #cfcfcf;
  display:flex;align-items:center;justify-content:center;text-align:center;
  font-size:14px;font-weight:700;line-height:24px;color:#555;
}

.control{
  position:absolute;display:flex;flex-direction:column;align-items:center;justify-content:flex-end;
  padding-bottom:8px;
  background:linear-gradient(var(--btn-top),var(--btn-bottom));
  border:1px solid var(--btn-border);border-radius:3px;
  font-size:16px;color:#333;
}
.control svg{margin-bottom:6px}
.control--unavailable{
  background:linear-gradient(var(--off-top),var(--off-bottom));
  border:2px solid var(--off-border);
  box-shadow:inset 0 0 0 1px #9a9a9a;
  color:var(--off-text);
}
.control--online{left:0;top:200px;width:149px;height:93px}
.control--run{left:160px;top:200px;width:149px;height:93px}
.control--stop{left:0;top:305px;width:149px;height:95px}
.control--auto{left:160px;top:305px;width:149px;height:95px}
.control .count{color:var(--navy)}

.status{
  position:absolute;left:0;top:409px;width:309px;height:48px;
  background:linear-gradient(var(--header-top),var(--header-bottom));
  color:#fff;font-size:21px;font-weight:600;
  display:flex;align-items:center;padding-left:18px;
}

.readings{position:absolute;left:0;top:460px;width:309px;height:211px;background:var(--panel-white)}
.engine{position:absolute;left:0;top:0;width:180px;height:211px;border-right:2px solid var(--rule)}
.engine-row{height:52.75px;border-bottom:2px solid var(--rule);position:relative;padding-left:50px;padding-top:6px}
.engine-row:last-child{border-bottom:none}
.engine-row svg{position:absolute;left:8px;top:12px}
.engine-label{font-size:19px;font-weight:700;color:var(--text-dark);line-height:22px}
.engine-value{font-size:17px;color:var(--text-mid);line-height:21px;word-spacing:10px}

.electric{position:absolute;left:182px;top:0;width:127px;height:211px}
.electric-group{border-bottom:2px solid var(--rule);padding:4px 0}
.electric-group:last-child{border-bottom:none}
.electric-group--voltage{height:80px}
.electric-group--current{height:78px}
.electric-line{display:flex;font-size:17px;line-height:24px;color:var(--text-dark)}
.electric-line .num{width:66px;text-align:right;padding-right:6px}

.meter{position:absolute;left:315px;top:193px;width:40px;height:480px;background:var(--scale-bg);border:1px solid #dcdcdc}
.meter-fill{
  position:absolute;left:0;right:0;bottom:0;height:310px;
  background:repeating-linear-gradient(-55deg,var(--green) 0 6px,var(--green-light) 6px 10px);
}
.meter-fill-label{
  position:absolute;left:0;right:0;top:0;height:27px;background:var(--green-dark);
  color:#fff;font-weight:700;font-size:16px;text-align:center;line-height:27px;
}
.scale{position:absolute;left:356px;top:193px;width:39px;height:480px;background:#fff;border-left:1px solid #bbb}
.tick{position:absolute;left:0;width:100%;border-top:1px solid #d8d8d8;font-size:11px;color:#666;padding-left:3px;line-height:13px}
.tick-kw{position:absolute;left:3px;bottom:2px;font-size:11px;color:#666}
</style>
</head>
<body>

<!-- Offline generator panel -->
<section class="panel panel--offline">
  <div class="breaker">Circuit<br>Breaker<br>Open</div>

  <div class="control control--online">
    <svg width="44" height="46" viewBox="0 0 44 46"><path d="M8 20a14 14 0 0 1 25-8l4-4v13H24l5-5a9 9 0 0 0-16 5z" fill="var(--green)"/><path d="M36 26a14 14 0 0 1-25 8l-4 4V25h13l-5 5a9 9 0 0 0 16-5z" fill="var(--blue)"/></svg>
    Run Online
  </div>
  <div class="control control--run">
    <svg width="48" height="46" viewBox="0 0 48 46"><circle cx="18" cy="18" r="12" fill="none" stroke="var(--orange)" stroke-width="7" stroke-dasharray="5 4"/><circle cx="18" cy="18" r="9" fill="var(--orange)"/><circle cx="18" cy="18" r="4" fill="#fff"/><circle cx="34" cy="32" r="8" fill="none" stroke="var(--blue)" stroke-width="5" stroke-dasharray="4 3"/><circle cx="34" cy="32" r="6" fill="var(--blue)"/><circle cx="34" cy="32" r="2.5" fill="#fff"/></svg>
    Run
  </div>
  <div class="control control--stop">
    <svg width="44" height="44" viewBox="0 0 44 44"><circle cx="22" cy="22" r="19" fill="var(--red)"/><circle cx="22" cy="22" r="12" fill="#fff"/><path d="M13 13l18 18" stroke="var(--red)" stroke-width="6"/></svg>
    Stop
  </div>
  <div class="control control--auto">
    <svg width="48" height="46" viewBox="0 0 48 46"><circle cx="24" cy="20" r="15" fill="var(--blue)"/><ellipse cx="24" cy="20" rx="7" ry="15" fill="none" stroke="#cfe3f7" stroke-width="2"/><path d="M9 20h30" stroke="#cfe3f7" stroke-width="2"/><path d="M33 5a17 17 0 0 1 6 6" stroke="var(--red)" stroke-width="3" fill="none"/><rect x="12" y="36" width="24" height="5" rx="2" fill="#444"/></svg>
    <span>Automatic <span class="count">(1)</span></span>
  </div>

  <div class="status">Running - Offline</div>

  <div class="readings">
    <div class="engine">
      <div class="engine-row">
        <svg width="22" height="30" viewBox="0 0 22 30"><rect x="8" y="2" width="6" height="18" rx="3" fill="#bcd9f0" stroke="#6a8fb0"/><circle cx="11" cy="23" r="5" fill="#4a90d0"/></svg>
        <div class="engine-label">Water Temp</div><div class="engine-value">83 °C</div>
      </div>
      <div class="engine-row">
        <svg width="26" height="26" viewBox="0 0 26 26"><circle cx="13" cy="13" r="11" fill="#d8d8d8" stroke="#555" stroke-width="2"/><path d="M13 13l5-5" stroke="#c0392b" stroke-width="2"/></svg>
        <div class="engine-label">Oil Pressure</div><div class="engine-value">3.8 BAR</div>
      </div>
      <div class="engine-row">
        <svg width="26" height="26" viewBox="0 0 26 26"><circle cx="13" cy="13" r="11" fill="#444"/><path d="M5 13a8 8 0 0 1 16 0" stroke="#c0392b" stroke-width="3" fill="none"/><path d="M13 13l4-5" stroke="#7ac231" stroke-width="2"/></svg>
        <div class="engine-label">RPM</div><div class="engine-value">1500</div>
      </div>
      <div class="engine-row">
        <svg width="26" height="26" viewBox="0 0 26 26"><circle cx="13" cy="13" r="10" fill="none" stroke="#555" stroke-width="2"/><path d="M13 7v6h5" stroke="#555" stroke-width="2" fill="none"/></svg>
        <div class="engine-label">Online Time</div><div class="engine-value">0h 0m 0s</div>
      </div>
    </div>
    <div class="electric">
      <div class="electric-group electric-group--voltage">
        <div class="electric-line"><span class="num">230</span>VAC</div>
        <div class="electric-line"><span class="num">400</span>VAC</div>
        <div class="electric-line"><span class="num">50.0</span>HZ</div>
      </div>
      <div class="electric-group electric-group--current">
        <div class="electric-line"><span class="num">0</span>A L1</div>
        <div class="electric-line"><span class="num">0</span>A L2</div>
        <div class="electric-line"><span class="num">0</span>A L3</div>
      </div>
      <div class="electric-group">
        <div class="electric-line"><span class="num">0</span>KVA</div>
        <div class="electric-line"><span class="num">0.00</span>PF</div>
      </div>
    </div>
  </div>

  <div class="meter"></div>
  <div class="scale">
    <div class="tick" style="top:0;border-top:none">100%</div>
    <div class="tick" style="top:96px">80%</div>
    <div class="tick" style="top:191px">60%</div>
    <div class="tick" style="top:286px">40%</div>
    <div class="tick" style="top:382px">20%</div>
    <div class="tick-kw">0 KW</div>
  </div>
</section>

<!-- Online generator panel -->
<section class="panel panel--online">
  <div class="breaker">Circuit<br>Breaker<br>Close</div>

  <div class="control control--online">
    <svg width="44" height="46" viewBox="0 0 44 46"><path d="M8 20a14 14 0 0 1 25-8l4-4v13H24l5-5a9 9 0 0 0-16 5z" fill="var(--green)"/><path d="M36 26a14 14 0 0 1-25 8l-4 4V25h13l-5 5a9 9 0 0 0 16-5z" fill="var(--blue)"/></svg>
    Run Online
  </div>
  <div class="control control--run control--unavailable">
    <svg width="48" height="46" viewBox="0 0 48 46"><circle cx="22" cy="20" r="13" fill="none" stroke="#7a7a7a" stroke-width="8" stroke-dasharray="5 4"/><circle cx="22" cy="20" r="10" fill="#7a7a7a"/><circle cx="22" cy="20" r="4" fill="#bbb"/></svg>
    Run
  </div>
  <div class="control control--stop control--unavailable">
    <svg width="44" height="44" viewBox="0 0 44 44"><circle cx="22" cy="22" r="19" fill="#7a7a7a"/><circle cx="22" cy="22" r="12" fill="#bdbdbd"/><path d="M13 13l18 18" stroke="#7a7a7a" stroke-width="6"/></svg>
    Stop
  </div>
  <div class="control control--auto">
    <svg width="48" height="46" viewBox="0 0 48 46"><circle cx="24" cy="20" r="15" fill="var(--blue)"/><ellipse cx="24" cy="20" rx="7" ry="15" fill="none" stroke="#cfe3f7" stroke-width="2"/><path d="M9 20h30" stroke="#cfe3f7" stroke-width="2"/><path d="M33 5a17 17 0 0 1 6 6" stroke="var(--red)" stroke-width="3" fill="none"/><rect x="12" y="36" width="24" height="5" rx="2" fill="#444"/></svg>
    <span>Automatic <span class="count">(1)</span></span>
  </div>

  <div class="status">Running - Online</div>

  <div class="readings">
    <div class="engine">
      <div class="engine-row">
        <svg width="22" height="30" viewBox="0 0 22 30"><rect x="8" y="2" width="6" height="18" rx="3" fill="#bcd9f0" stroke="#6a8fb0"/><circle cx="11" cy="23" r="5" fill="#4a90d0"/></svg>
        <div class="engine-label">Water Temp</div><div class="engine-value">83 °C</div>
      </div>
      <div class="engine-row">
        <svg width="26" height="26" viewBox="0 0 26 26"><circle cx="13" cy="13" r="11" fill="#d8d8d8" stroke="#555" stroke-width="2"/><path d="M13 13l5-5" stroke="#c0392b" stroke-width="2"/></svg>
        <div class="engine-label">Oil Pressure</div><div class="engine-value">3.8 BAR</div>
      </div>
      <div class="engine-row">
        <svg width="26" height="26" viewBox="0 0 26 26"><circle cx="13" cy="13" r="11" fill="#444"/><path d="M5 13a8 8 0 0 1 16 0" stroke="#c0392b" stroke-width="3" fill="none"/><path d="M13 13l4-5" stroke="#7ac231" stroke-width="2"/></svg>
        <div class="engine-label">RPM</div><div class="engine-value">1500</div>
      </div>
      <div class="engine-row">
        <svg width="26" height="26" viewBox="0 0 26 26"><circle cx="13" cy="13" r="10" fill="none" stroke="#555" stroke-width="2"/><path d="M13 7v6h5" stroke="#555" stroke-width="2" fill="none"/></svg>
        <div class="engine-label">Online Time</div><div class="engine-value">0h 3m 33s</div>
      </div>
    </div>
    <div class="electric">
      <div class="electric-group electric-group--voltage">
        <div class="electric-line"><span class="num">230</span>VAC</div>
        <div class="electric-line"><span class="num">400</span>VAC</div>
        <div class="electric-line"><span class="num">50.0</span>HZ</div>
      </div>
      <div class="electric-group electric-group--current">
        <div class="electric-line"><span class="num">15</span>A L1</div>
        <div class="electric-line"><span class="num">22</span>A L2</div>
        <div class="electric-line"><span class="num">19</span>A L3</div>
      </div>
      <div class="electric-group">
        <div class="electric-line"><span class="num">45</span>KVA</div>
        <div class="electric-line"><span class="num">0.00</span>PF</div>
      </div>
    </div>
  </div>

  <div class="meter">
    <div class="meter-fill"><div class="meter-fill-label">63%</div></div>
  </div>
  <div class="scale">
    <div class="tick" style="top:0;border-top:none">100%</div>
    <div class="tick" style="top:96px">80%</div>
    <div class="tick" style="top:191px">60%</div>
    <div class="tick" style="top:286px">40%</div>
    <div class="tick" style="top:382px">20%</div>
    <div class="tick-kw">41 KW</div>
  </div>
</section>

</body>
</html>
```